Acai Bowl and Coffee Van need new Menus

We currently have a basic menu that is displayed in an A3 frame. It lacks images, specifically of the Acai Bowls and is difficult to read and understand.

We need a new Acai Bowl Menu and a new Drink Menu but in a more attractive and easier to read format.
We would like images of the Acai Bowls (using Images supplied or make your own) in order to show customers what is on each bowl. Customers chose what granola they would like from the three that are available. Currently we tell customers to check the bottom of the menu as they are often unaware they get to chose.

The drink menu items are simple (we have removed smoothies from our menu entirely).
The drink menu needs to have "Chai Latte" and "Dirty Chai Latte" added as options with the same S,M,L pricing as a Latte.

I have attached images of the menus and a photo of how the menus are displayed on The Moro Cart. Also attached is photos of the Acai Bowls and other food / drink items on the menu if you wish to use them in your design. I have included the files for all of our logo variations.

Our main objective with the menu redesign is to have the menu more appealing and easier to read and understand.

Industry/Entity Type

Food and Coffee

Font styles to use
Other font styles liked:
• Orplid Pro (Fill and Shadow), Trend Sans One

Colors

Designer to choose colors to be used in the design.

Requirements
Must have
• The final design must include prices and be editable in the case of any price changes in the future.

```html
<!DOCTYPE html>
<html lang="en">
<head>
<meta charset="utf-8">
<title>The Moro Cart – Menus</title>
<link href="https://fonts.googleapis.com/css2?family=Josefin+Sans:wght@400;600;700&family=Nunito+Sans:ital,wght@0,400;0,600;1,700&display=swap" rel="stylesheet">
<style>
:root{
  --paper:#ffffff;
  --frame:#2b2b2b;
  --taupe:#a68e6e;
  --taupe-dark:#8a7358;
  --rule:#b9a995;
  --pink:#c9677a;
  --pink-soft:#f2e1e5;
  --banner:#c9636f;
  --ink:#5e4c3a;
  --shadow:#e3d2bf;
}
*{box-sizing:border-box;margin:0;padding:0}
html,body{width:1200px;height:811px;overflow:hidden;background:var(--paper)}
body{position:relative;font-family:"Nunito Sans",sans-serif;color:var(--ink)}
.abs{position:absolute}
.menu-sheet{position:absolute;top:19px;width:552px;height:780px;border:1.2px solid var(--frame);background:var(--paper);overflow:hidden}
.sheet-bowls{left:19px}
.sheet-drinks{left:629px}
.rule{position:absolute;height:1px;background:var(--rule)}
.vrule{position:absolute;width:1px;background:var(--rule)}
.brand{position:absolute;width:86px;height:86px;border-radius:50%;background:var(--pink-soft);display:flex;align-items:center;justify-content:center;text-align:center;font-family:"Josefin Sans",sans-serif;font-weight:600;font-size:12px;line-height:1.15;letter-spacing:1px;color:var(--taupe-dark);text-transform:uppercase}
.display{font-family:"Josefin Sans",sans-serif;font-weight:700;color:var(--paper);-webkit-text-stroke:1.1px var(--taupe);text-shadow:2px 2px 0 var(--shadow);text-transform:uppercase;white-space:nowrap;text-align:center;line-height:1}
.display.pink{-webkit-text-stroke-color:var(--pink);text-shadow:1.5px 1.5px 0 #f0d3da}
.section-head{font-size:19px;letter-spacing:.5px}
.hours{position:absolute;width:90px;text-align:center;font-family:"Josefin Sans",sans-serif;font-weight:600;color:#d49aa5;letter-spacing:2px;line-height:1.05;text-transform:uppercase}
.hours .big{font-size:14px;display:block}
.hours .small{font-size:10.5px;display:block;margin-top:2px}
.photo{position:absolute}
.bowl{position:absolute;width:112px}
.bowl-name{font-family:"Josefin Sans",sans-serif;font-weight:600;font-size:12px;letter-spacing:1.8px;line-height:14.5px;color:var(--taupe-dark);text-transform:uppercase}
.bowl-desc{font-size:7.4px;line-height:8.9px;margin-top:3px;color:var(--ink)}
.bowl-note{font-size:6.4px;line-height:8px;margin-top:7px;font-style:italic;font-weight:700;color:var(--pink)}
.bowl-tip{font-size:7.4px;line-height:8.9px;margin-top:9px}
.topping-price{position:absolute;font-size:18px}
.topping-list{position:absolute;font-size:9.2px;line-height:11px;display:grid;column-gap:6px}
.topping-list span::before{content:"• ";color:var(--pink)}
.granola-name{position:absolute;left:285px;font-size:11px;letter-spacing:.3px;text-align:left}
.granola-desc{position:absolute;left:285px;width:266px;font-size:9.3px;line-height:11px}
.diet-badges{position:absolute;left:392px;top:573px;width:136px;height:51px;border-radius:6px;background:var(--pink-soft);display:flex;justify-content:space-around;padding:5px 2px 0}
.badge{width:33px;text-align:center;font-family:"Josefin Sans",sans-serif;font-weight:600;font-size:5.2px;letter-spacing:.4px;line-height:6.5px;color:var(--taupe-dark);text-transform:uppercase}
.badge svg{display:block;margin:0 auto 3px}
.promo{position:absolute;left:89px;top:123px;width:372px;height:17px;border-radius:9px;background:var(--banner);color:#fff;font-family:"Josefin Sans",sans-serif;font-weight:600;font-size:9px;letter-spacing:.8px;text-align:center;line-height:18px;text-transform:uppercase;white-space:nowrap}
.price-table{position:absolute;font-size:9.4px;line-height:14px;text-transform:uppercase}
.price-table .row{display:grid}
.price-table .row span:not(:first-child){text-align:center}
.price-table .sub{font-size:7px;line-height:8px;text-transform:none}
.note-line{position:absolute;font-size:7.2px;white-space:nowrap}
</style>
</head>
<body>

<section class="menu-sheet sheet-bowls" aria-label="Acai bowls menu">
  <div class="rule" style="left:24px;top:23px;width:504px"></div>
  <div class="rule" style="left:24px;top:131px;width:504px"></div>
  <div class="brand" style="left:28px;top:32px">The Moro<br>Cart</div>
  <div class="vrule" style="left:130px;top:35px;height:82px"></div>
  <div class="display abs" style="left:145px;top:33px;width:260px;font-size:36px;letter-spacing:1px">Acai Bowls</div>
  <div class="display abs" style="left:145px;top:76px;width:260px;font-size:44px;letter-spacing:1px">Menus</div>
  <div class="vrule" style="left:436px;top:35px;height:82px"></div>
  <div class="hours" style="left:439px;top:48px"><span class="big">Open</span><span class="big">Hours</span><span class="small">From 11am</span><span class="small">to 6pm</span></div>

  <div class="photo" role="img" aria-label="Photo of hands holding an acai bowl topped with banana, berries and granola on a wooden table" style="left:24px;top:143px;width:161px;height:402px;background:linear-gradient(160deg,#a9876b 0%,#8b6448 40%,#7a2f3d 62%,#6d4a35 85%,#4e3526 100%)"></div>

  <div class="photo" role="img" aria-label="Photo of the original bowl with strawberry and granola" style="left:199px;top:141px;width:72px;height:73px;background:radial-gradient(circle at 50% 55%,#c4955e 0%,#9d3b3b 35%,#e9e2d6 55%,#6b5646 100%)"></div>
  <div class="photo" role="img" aria-label="Photo of the tropical bowl with passionfruit and mango" style="left:316px;top:141px;width:72px;height:73px;background:radial-gradient(circle at 50% 55%,#e0b43c 0%,#d99a2a 30%,#ece6db 55%,#7b6451 100%)"></div>
  <div class="photo" role="img" aria-label="Photo of the berry bowl with coconut, goji berries and blueberries" style="left:435px;top:141px;width:72px;height:73px;background:radial-gradient(circle at 50% 55%,#f3f0ec 0%,#8d2c3c 35%,#e8e2d9 55%,#5a4738 100%)"></div>
  <div class="photo" role="img" aria-label="Photo of the choc bowl with cacao and nut spread" style="left:199px;top:336px;width:72px;height:72px;background:radial-gradient(circle at 50% 55%,#4a2d22 0%,#9c6b4a 35%,#ece5da 55%,#6b5646 100%)"></div>
  <div class="photo" role="img" aria-label="Photo of the spekko bowl with biscuit crumble and goji berries" style="left:316px;top:336px;width:72px;height:72px;background:radial-gradient(circle at 50% 55%,#b07a45 0%,#8f3a2c 35%,#ebe3d8 55%,#7a6450 100%)"></div>
  <div class="photo" role="img" aria-label="Photo of the moro favourite bowl with protein slice and strawberry" style="left:435px;top:336px;width:72px;height:72px;background:radial-gradient(circle at 50% 55%,#d5a66a 0%,#b3463f 35%,#ede7dd 55%,#6c5849 100%)"></div>

  <div class="bowl" style="left:199px;top:218px">
    <div class="bowl-name">Original<br>Bowl<br>$17.50</div>
    <div class="bowl-desc">Açai Base Topped with Your Choice Of Granola, Coconut Flakes And Fresh Seasonal Fruit A Basic Bowl, Great For You To Start Your Own Creation</div>
  </div>
  <div class="bowl" style="left:316px;top:217px">
    <div class="bowl-name">Tropical<br>Bowl<br>$18.50</div>
    <div class="bowl-desc">Açai Base Topped with Your Choice Of Granola, Shredded Coconut. Passionfruit. Mango And Pineapple</div>
    <div class="bowl-note">Make It Extra Refreshing By Adding Some Kiwifruit For $1.00</div>
  </div>
  <div class="bowl" style="left:435px;top:217px">
    <div class="bowl-name">Berry Bowl<br>$18.50</div>
    <div class="bowl-desc">Açai Base Topped With Your Choice Of Granola, Shredded Coconut, Goji Berries, Strawberry And Blueberry</div>
    <div class="bowl-note">Add Some Cacao Nibs For An Extra $1.00</div>
  </div>
  <div class="bowl" style="left:199px;top:413px">
    <div class="bowl-name">Choc Bowl<br>$20.50</div>
    <div class="bowl-desc">Açai Base Topped with Your Choice Of Granola, Shredded Coconut, Cacao Nibs, Banana, Strawberry And Nutty Choc</div>
    <div class="bowl-tip">We Recommend The Cacao, Hazelnut And Chia Granola with This One</div>
  </div>
  <div class="bowl" style="left:316px;top:412px">
    <div class="bowl-name">Spekko Bowl<br>$21.00</div>
    <div class="bowl-desc">Açai Base, Topped with Your Choice Of Granola, Banana, Shredded Coconut, Goji Berries With Spekko Spread And Crumble</div>
    <div class="bowl-tip">If You Love Peanut Butter, You Will Love This Bowl Too</div>
  </div>
  <div class="bowl" style="left:435px;top:412px">
    <div class="bowl-name">Moro<br>Favourite<br>$21.00</div>
    <div class="bowl-desc">Açai Base, Topped with Your Choice Of Granola, Coconut Flakes, Goji Berries, Chia Seeds, Banana, Strawberry And Peanut Butter</div>
    <div class="bowl-note">Add A Peanut Butter Protein Slice On Top For $2.50</div>
  </div>

  <div class="rule" style="left:24px;top:554px;width:504px"></div>

  <div class="display abs" style="left:24px;top:566px;font-size:19px;letter-spacing:.5px;text-align:left;line-height:21px">Additional<br>Toppings</div>
  <div class="rule" style="left:24px;top:615px;width:225px"></div>
  <div class="display pink topping-price" style="left:24px;top:624px">0.50</div>
  <div class="topping-list" style="left:67px;top:622px;grid-template-columns:auto auto"><span>Chia Seeds</span><span>Coconut Flakes</span><span>Bellvine Passionfruit</span><span>Shredded Coconut</span></div>
  <div class="rule" style="left:24px;top:651px;width:225px"></div>
  <div class="topping-list" style="left:24px;top:657px;grid-template-columns:auto auto auto"><span>Goji Berries</span><span>Honey</span><span>Extra Fruit</span><span>Cacao Nibs</span><span>Dates</span><span>Extra Granola</span></div>
  <div class="display pink topping-price" style="left:207px;top:660px">1.00</div>
  <div class="rule" style="left:24px;top:686px;width:225px"></div>
  <div class="display pink topping-price" style="left:24px;top:695px">2.00</div>
  <div class="topping-list" style="left:71px;top:692px;grid-template-columns:auto auto;column-gap:10px"><span>Peanut Butter</span><span>Nutty Choc</span><span>Almond Butter</span><span>Spekko</span></div>
  <div class="rule" style="left:24px;top:721px;width:225px"></div>
  <div class="photo" role="img" aria-label="Photo of a peanut butter protein slice" style="left:23px;top:718px;width:46px;height:43px;background:linear-gradient(135deg,#efe6dc 0%,#c9944f 45%,#6e4125 60%,#efe4d8 100%)"></div>
  <div class="abs" style="left:73px;top:729px;font-size:9.2px;line-height:11px">Shoreline Crunch Peanut Butter<br>Protein Slice</div>
  <div class="display pink topping-price" style="left:207px;top:731px">2.50</div>
  <div class="rule" style="left:24px;top:757px;width:225px"></div>

  <div class="vrule" style="left:257px;top:564px;height:211px"></div>
  <div class="display abs" style="left:285px;top:567px;font-size:17px;letter-spacing:.3px;text-align:left;line-height:20px">Shoreline<br>Crunch<br>Granola</div>

  <div class="diet-badges">
    <div class="badge"><svg width="22" height="22" viewBox="0 0 22 22" fill="none" stroke="#c9677a" stroke-width="1.2"><circle cx="11" cy="11" r="10"/><path d="M11 5v12M11 9l-3-2M11 9l3-2M11 12l-3-2M11 12l3-2M5 17L17 5"/></svg>Gluten<br>Free</div>
    <div class="badge"><svg width="22" height="22" viewBox="0 0 22 22" fill="none" stroke="#c9677a" stroke-width="1.2"><circle cx="11" cy="11" r="10"/><path d="M9 5h4v2l1.5 2v8h-7V9L9 7z"/></svg>Dairy<br>Free</div>
    <div class="badge"><svg width="22" height="22" viewBox="0 0 22 22" fill="none" stroke="#c9677a" stroke-width="1.2"><circle cx="11" cy="11" r="10"/><rect x="6" y="9" width="5" height="5"/><rect x="11" y="7" width="5" height="5"/><path d="M5 17L17 5"/></svg>No Refined<br>Sugars</div>
    <div class="badge"><svg width="22" height="22" viewBox="0 0 22 22" fill="none" stroke="#c9677a" stroke-width="1.2"><circle cx="11" cy="11" r="10"/><path d="M7 7l4 9 4-10M13 8c1-1 2-2 3-2"/></svg>Vegan<br>Friendly</div>
  </div>

  <div class="display pink granola-name" style="top:643px">Gingernut Crunch</div>
  <div class="granola-desc" style="top:655px">Inspired by Beloved Ginger Nut Biscuits, This Granola Brings The Warmth and Comfort of Ginger, Nutmeg, and Cinnamon to Your Favourite Bowl.</div>
  <div class="display pink granola-name" style="top:692px">Toasted Almond &amp; Cinnamon</div>
  <div class="granola-desc" style="top:704px">Combines The Warmth of Cinnamon with Toasted Aussie Almonds and 100% WA Grown Lupin Flakes</div>
  <div class="display pink granola-name" style="top:730px">Cacao, Hazelnut &amp; Chia</div>
  <div class="granola-desc" style="top:742px">One for The Chocolate Lovers, Tastes Like A Crunchy Version of Nutty Choc with Hazelnuts and Cacao.</div>
</section>

<section class="menu-sheet sheet-drinks" aria-label="Drink menu">
  <div class="rule" style="left:24px;top:23px;width:504px"></div>
  <div class="rule" style="left:24px;top:131px;width:504px"></div>
  <div class="brand" style="left:28px;top:32px">The Moro<br>Cart</div>
  <div class="vrule" style="left:130px;top:35px;height:82px"></div>
  <div class="display abs" style="left:150px;top:33px;width:260px;font-size:36px;letter-spacing:1px">Drink</div>
  <div class="display abs" style="left:150px;top:76px;width:260px;font-size:44px;letter-spacing:1px">Menus</div>
  <div class="vrule" style="left:436px;top:35px;height:82px"></div>
  <div class="hours" style="left:439px;top:48px"><span class="big">Open</span><span class="big">Hours</span><span class="small">From 11am</span><span class="small">to 6pm</span></div>
  <div class="promo">Bring a reusable cup and get 50 cents off your coffee!</div>

  <div class="photo" role="img" aria-label="Photo of many coffee cups with latte art on a weathered wooden table" style="left:23px;top:151px;width:250px;height:269px;background:radial-gradient(circle at 55% 40%,#e8d8c2 0%,#c79a6b 25%,#6e5a4a 50%,#d8d1c6 75%,#3b2e25 100%)"></div>

  <div class="display abs section-head" style="left:290px;top:151px;width:234px">Cold Beverages</div>
  <div class="price-table" style="left:300px;top:180px">
    <div class="row" style="grid-template-columns:110px 42px 62px"><span></span><span>Regular</span><span>Large</span></div>
    <div class="row" style="grid-template-columns:110px 42px 62px"><span>Cold Brew Coffee</span><span>6.50</span><span>8.50</span></div>
    <div class="row" style="grid-template-columns:110px 42px 62px"><span>Iced Coffee</span><span>6.50</span><span>7.50</span></div>
    <div class="row" style="grid-template-columns:110px 42px 62px"><span>Iced Mocha</span><span>6.50</span><span>7.50</span></div>
    <div class="row" style="grid-template-columns:110px 42px 62px"><span>Iced Long Black</span><span>5.50</span><span>6.50</span></div>
    <div class="row" style="grid-template-columns:110px 42px 62px"><span>Iced Chocolate</span><span>6.50</span><span>7.50</span></div>
    <div class="row" style="grid-template-columns:110px 42px 62px"><span>Iced Pure Tea</span><span>5.00</span><span>6.00</span></div>
  </div>
  <div class="note-line" style="left:300px;top:279px">Lemongrass and Ginger &nbsp;|&nbsp; White Tea, Acai and Coconut &nbsp;|&nbsp; Chai</div>

  <div class="display abs section-head" style="left:290px;top:304px;width:234px">Alternative Milks</div>
  <div class="price-table" style="left:300px;top:333px">
    <div class="row" style="grid-template-columns:110px 42px"><span>Oat Milk</span><span>0.70</span></div>
    <div class="sub">Grove Dairy Co</div>
    <div class="row" style="grid-template-columns:110px 42px;margin-top:1px"><span>Almond Milk</span><span>0.70</span></div>
    <div class="sub">Pour Lab</div>
    <div class="row" style="grid-template-columns:110px 42px;margin-top:1px"><span>Soy Milk</span><span>0.70</span></div>
    <div class="sub">Sunny Day Soy Co</div>
    <div class="row" style="grid-template-columns:110px 42px;margin-top:1px"><span>Lactose Free</span><span>0.70</span></div>
    <div class="sub">Pour Lab</div>
  </div>

  <div class="display abs section-head" style="left:60px;top:437px;width:190px">Coffee</div>
  <div class="price-table" style="left:24px;top:464px">
    <div class="row" style="grid-template-columns:114px 50px 50px 50px"><span></span><span>Small</span><span>Regular</span><span>Large</span></div>
    <div class="row" style="grid-template-columns:114px 50px 50px 50px"><span>Cappuccino</span><span>5.50</span><span>6.50</span><span>7.50</span></div>
    <div class="row" style="grid-template-columns:114px 50px 50px 50px"><span>Latte</span><span>5.50</span><span>6.50</span><span>7.50</span></div>
    <div class="row" style="grid-template-columns:114px 50px 50px 50px"><span>Chai Latte</span><span>5.50</span><span>6.50</span><span>7.50</span></div>
    <div class="row" style="grid-template-columns:114px 50px 50px 50px"><span>Dirty Chai Latte</span><span>5.50</span><span>6.50</span><span>7.50</span></div>
    <div class="row" style="grid-template-columns:114px 50px 50px 50px"><span>Flat White</span><span>5.50</span><span>6.50</span><span>7.50</span></div>
    <div class="row" style="grid-template-columns:114px 50px 50px 50px"><span>Espresso</span><span>4.00</span><span>4.50</span><span>5.00</span></div>
    <div class="row" style="grid-template-columns:114px 50px 50px 50px"><span>Long Black</span><span>4.50</span><span>5.00</span><span>5.50</span></div>
    <div class="row" style="grid-template-columns:114px 50px 50px 50px"><span>Macchiato</span><span></span><span>5.50</span><span>6.00</span></div>
  </div>

  <div class="display abs section-head" style="left:45px;top:606px;width:195px">Chocolate</div>
  <div class="price-table" style="left:24px;top:631px">
    <div class="row" style="grid-template-columns:114px 50px 50px 50px"><span></span><span>Small</span><span>Regular</span><span>Large</span></div>
    <div class="row" style="grid-template-columns:114px 50px 50px 50px"><span>Mocha</span><span>5.50</span><span>6.50</span><span>7.50</span></div>
    <div class="row" style="grid-template-columns:114px 50px 50px 50px"><span>Hot Chocolate</span><span>5.00</span><span>6.00</span><span>7.00</span></div>
  </div>

  <div class="display abs section-head" style="left:60px;top:688px;width:190px">Extras</div>
  <div class="price-table" style="left:23px;top:712px">
    <div class="row" style="grid-template-columns:114px 50px"><span>Additional Shot</span><span>0.50</span></div>
    <div class="row" style="grid-template-columns:114px 50px"><span>Shot of Syrup</span><span>0.50</span></div>
  </div>
  <div class="note-line" style="left:23px;top:742px">Vanilla | Caramel | Hazelnut</div>

  <div class="photo" role="img" aria-label="Photo of a glass cup of amber black tea" style="left:300px;top:444px;width:109px;height:104px;background:radial-gradient(circle at 45% 55%,#d8792a 0%,#b9561c 25%,#e8e2da 50%,#f2efea 100%)"></div>
  <div class="photo" role="img" aria-label="Photo of a glass cup of green tea with fresh leaves" style="left:417px;top:444px;width:110px;height:104px;background:radial-gradient(circle at 45% 55%,#a2b84a 0%,#5e8a2f 30%,#b8b2a8 55%,#8f8a80 100%)"></div>

  <div class="display abs section-head" style="left:305px;top:561px;width:220px">Pure Tea</div>
  <div class="price-table" style="left:300px;top:589px;line-height:13px">
    <div class="row" style="grid-template-columns:110px 42px"><span></span><span>Regular</span></div>
    <div class="row" style="grid-template-columns:110px 42px"><span>English Breakfast</span><span>4.00</span></div>
    <div class="row" style="grid-template-columns:110px 42px"><span>Morning Dew</span><span>4.00</span></div>
    <div class="row" style="grid-template-columns:110px 42px"><span>Gunpowder Green</span><span>4.00</span></div>
    <div class="row" style="grid-template-columns:110px 42px"><span>Chaitea</span><span>4.00</span></div>
    <div class="row" style="grid-template-columns:110px 42px"><span>Peppermint</span><span>4.00</span></div>
    <div class="row" style="grid-template-columns:110px 42px"><span>Cocao &amp; Peppermint</span><span>4.00</span></div>
  </div>

  <div class="display abs section-head" style="left:290px;top:696px;width:234px">More Beverages</div>
  <div class="price-table" style="left:300px;top:725px;line-height:13px">
    <div class="row" style="grid-template-columns:110px 42px"><span>Tonic Kombucha</span><span>4.50</span></div>
    <div class="row" style="grid-template-columns:110px 42px"><span>Bottled Water</span><span>3.00</span></div>
  </div>
</section>

</body>
</html>
```